updated documents

Hi i have included a new picture for the about us section, i have also included the updated word document, all changes have been highlighted.

Thanks,

Leon

```html
<!DOCTYPE html>
<html lang="en">
<head>
<meta charset="utf-8">
<title>Services – Crestline Property Services</title>
<link href="https://fonts.googleapis.com/css2?family=Cinzel:wght@400;500&family=Questrial&display=swap" rel="stylesheet">
<style>
  :root {
    --paper: #ffffff;
    --lime: #a6cc3a;
    --band-grey: #e3e3e4;
    --roof-grey: #6d6e70;
    --roof-light: #e1e1e2;
    --ink: #222222;
    --body: #6a6a6a;
    --dot: #ececec;
    --frame: #f2f2f2;
    --fold: #444444;
  }
  * { margin: 0; padding: 0; box-sizing: border-box; }
  html, body { width: 1200px; height: 850px; overflow: hidden; background: var(--paper); }
  .spread {
    position: relative; width: 1200px; height: 850px; overflow: hidden;
    background: var(--paper); border: 1px solid var(--fold);
  }
  .shapes { position: absolute; inset: 0; }
  .fold { position: absolute; left: 600px; top: 0; width: 1px; height: 850px; background: var(--fold); }
  .dot-row {
    position: absolute; left: 20px; right: 20px; height: 12px;
    background-image: radial-gradient(circle, var(--dot) 4.5px, transparent 5px);
    background-size: 22.5px 12px;
  }
  .dot-row.top { top: 23px; }
  .dot-row.bottom { bottom: 22px; }
  .page-title {
    position: absolute; left: 118px; top: 68px;
    font-family: "Cinzel", serif; font-weight: 500; font-size: 29px;
    color: var(--paper); letter-spacing: 1px;
  }
  .service { position: absolute; width: 262px; }
  .service h2 {
    font-family: "Cinzel", serif; font-weight: 500; font-size: 12.6px;
    color: var(--ink); letter-spacing: 0.6px; margin-bottom: 3px; line-height: 1.1;
  }
  .service p {
    font-family: "Questrial", sans-serif; font-size: 8.4px; line-height: 12.1px;
    color: var(--body);
  }
  .photo {
    position: absolute; width: 134px; height: 85px;
    border: 2px solid var(--frame); box-shadow: 2px 2px 3px rgba(0,0,0,0.18);
  }
  .left .photo { left: 117px; }
  .left .service { left: 266px; }
  .right .photo { left: 714px; }
  .right .service { left: 865px; }
</style>
</head>
<body>
<div class="spread">
  <svg class="shapes" width="1200" height="850" viewBox="0 0 1200 850" aria-hidden="true">
    <polygon points="352,0 422,0 0,402 0,348" fill="var(--band-grey)"/>
    <polygon points="174,0 352,0 0,348 0,156" fill="var(--lime)"/>
    <polygon points="1108,720 1136,720 1136,850 1108,850" fill="var(--roof-light)"/>
    <polygon points="532,850 844,608 992,740 992,692 1108,692 1108,850" fill="var(--roof-grey)"/>
    <polygon points="652,850 808,740 962,850" fill="var(--paper)"/>
  </svg>
  <div class="dot-row top"></div>
  <div class="dot-row bottom"></div>
  <div class="fold"></div>

  <section class="left">
    <h1 class="page-title">Services</h1>

    <div class="photo" style="top:129px;background:linear-gradient(160deg,#8fb3d8,#5a6f86 60%,#c86a2a);" role="img" aria-label="Workers in hard hats and high-visibility vests reviewing plans on a roof"></div>
    <div class="service" style="top:128px">
      <h2>Building Repairs and Maintenance</h2>
      <p>The team at Crestline Property Services have extensive skills and experience in both internal and external building repairs and maintenance. Installation and repairs to floor and ceilings systems, doors/locks, appliance repairs, whiteboards, TV screens, picture hanging, patching and paint, vandal repairs, workstations and joinery, plumbing and electrical.</p>
    </div>

    <div class="photo" style="top:218px;background:linear-gradient(90deg,#e9e9ea,#d8d8d9 50%,#ececed);" role="img" aria-label="Two hands joining an orange extension cable plug and socket"></div>
    <div class="service" style="top:236px">
      <h2>Electrical</h2>
      <p>Crestline Property Services provides a wide range of electrical services ranging from Test and tag, Mains services, Switchboard installations, fault finding, RCD testing, data cabling/patching, electrical upgrades and lighting.</p>
    </div>

    <div class="photo" style="top:307px;background:linear-gradient(180deg,#f2f2f2,#d9d8cf 60%,#a9a27a);" role="img" aria-label="Maintenance workers climbing outdoor stairs"></div>
    <div class="service" style="top:319px">
      <h2>Planned Preventative Maintenance</h2>
      <p>Crestline Property Services Offer planned preventive maintenance specifically tailored to the client's requirements. Planned maintenance schedules can be created to prevent breakdowns and costly reactive maintenance in the future. Maintenance programs can include floor and ceiling repairs, light bulb replacements, Test and tagging, Storm water and gutter cleaning.</p>
    </div>

    <div class="photo" style="top:396px;background:linear-gradient(120deg,#b9cfe9,#e4ecf5 55%,#f6f6f6);" role="img" aria-label="Woman painting a wall light blue with a roller"></div>
    <div class="service" style="top:426px">
      <h2>Painting</h2>
      <p>Crestline Property Services pride ourselves in quality and detail ensuring the very best results while being a cost effective and efficient.</p>
    </div>

    <div class="photo" style="top:485px;background:linear-gradient(160deg,#cfe0ee,#9cba7c 55%,#b8323a);" role="img" aria-label="Sold sign in front of a house"></div>
    <div class="service" style="top:497px">
      <h2>Signage</h2>
      <p>Crestline Property Services have an experience signage team that specialize in both internal and external signage, decals, promotional banners, window frosting, company logos and design.</p>
    </div>

    <div class="photo" style="top:574px;background:linear-gradient(140deg,#d9c8b5,#8a9a72 55%,#6f5a4a);" role="img" aria-label="Office team gathered around a desk planning a layout"></div>
    <div class="service" style="top:580px">
      <h2>Office Layout Changes</h2>
      <p>If you are looking to make some changes to your office either big or small our team can assist with Workstation reconfiguration, internal demolition, Partition/wall installations and even complete office relocations.</p>
    </div>

    <div class="photo" style="top:663px;background:linear-gradient(110deg,#f1f1f1,#d8d8d8 45%,#2f3c55);" role="img" aria-label="Technician repairing a kitchen appliance"></div>
    <div class="service" style="top:664px">
      <h2>Appliance Repairs</h2>
      <p>Crestline Property Services can repair and replace all of your office appliance's ranging from dishwashers and microwaves to monitors, TV's and projectors.</p>
    </div>
  </section>

  <section class="right">
    <div class="photo" style="top:129px;background:linear-gradient(130deg,#e6d6bd,#f3ede4 55%,#e98a3a);" role="img" aria-label="Gloved hands cleaning with a spray bottle and cloth"></div>
    <div class="service" style="top:128px">
      <h2>Cleaning</h2>
      <p>Our team offer both internal and external cleaning services including carpark cleaning, window cleaning, carpet dry cleaning, and general office cleaning.</p>
    </div>

    <div class="photo" style="top:218px;background:linear-gradient(100deg,#2f8a4a,#3aa05a 50%,#c9a57a);" role="img" aria-label="Man placing rubbish into a green wheelie bin"></div>
    <div class="service" style="top:200px">
      <h2>Rubbish Removal / Recycling</h2>
      <p>Crestline Property Services specialize in office rubbish removal. We have a solution to all your rubbish removal needs; including, electronic waste recycling (PCs, monitors, printers, cables etc.), Basement access skip bins, wheelie bins of various sizes, internal demolition services, workstation/furniture removal, rubbish removal/cleanup services.</p>
    </div>

    <div class="photo" style="top:307px;background:linear-gradient(130deg,#cfd6df,#e8e8e8 50%,#2f5f9a);" role="img" aria-label="Plumbers fitting a white drain pipe"></div>
    <div class="service" style="top:307px">
      <h2>Plumbing</h2>
      <p>Our Plumbing team are experienced and available 24/7 for all your plumbing requirements. Our plumbing services include, water boiler/chiller unit installs and repairs, blocked drains and toilets, roof work and gas fitting.</p>
    </div>

    <div class="photo" style="top:396px;background:radial-gradient(circle at 50% 55%,#5c8a2e 0,#c9a48a 22%,#3a3330 55%,#2b2522);" role="img" aria-label="Hands holding soil with a young green seedling"></div>
    <div class="service" style="top:390px">
      <h2>Grounds Keeping</h2>
      <p>Let us help with your grounds keeping, our services include, lawn mowing and garden care, carpark sweeping, tree pruning, line marking, gutter cleaning, landscaping, bird and pest management, fencing installs and repairs.</p>
    </div>

    <div class="photo" style="top:485px;background:linear-gradient(150deg,#6b4a34,#b98a66 50%,#c23a2a);" role="img" aria-label="Carpenter working with a red power tool in a workshop"></div>
    <div class="service" style="top:473px">
      <h2>Carpentry</h2>
      <p>Crestline Property Services have a dedicated carpentry team that can assist with all your requirements including Partitioning, cupboard installations and all repairs and modifications.</p>
    </div>

    <div class="photo" style="top:574px;background:linear-gradient(160deg,#f3f3f3,#e4dcd0 55%,#c98a3a);" role="img" aria-label="Worker measuring a floor with a tape measure"></div>
    <div class="service" style="top:544px">
      <h2>Floor / Ceiling</h2>
      <p>We can provide floor and ceiling repairs to all types of systems including, suspended ceiling systems and raised floors, ceiling/ floor tile replacement, carpet and vinyl replacements and repairs, ceiling access hatches and air vent installs.</p>
    </div>
  </section>
</div>
</body>
</html>
```